Psychology Practice Brochure and Letterhead
Quiet Harbor Psychological Services
I will have a submission in very shortly.
Sorry for the omission of our business contact information:
26840 W. 93rd St., Suite 410
Denbury Glen, IL 60512
Phone/Fax: 708.519.2483
info@quietharborpsych.example
#2,#7 and #8
*****Please note that we have shortened the "what to expect" section and alphabetized the items under the "what we treat" section. The new wording has been uploaded and is in the brief, along with some pictures and quotes we would like you to incorporate.
Thank you so much for your hard work on our project! We really like the green curved lines of #8 because it ties all the sections together. Could you put the "do i need therapy" section on the left outside panel? Then, you can move the "what to expect" section to the middle section with a map. Also, we really like the different shades of blue that you put behind the different text sections of #2 because it makes it easier to read.Thanks
Hello designers! We are so excited about your creative ideas for the brochure.
*****Please note that we have changed the brochure wording slightly, so please edit the text in your submissions. The changes are as follows:
1) The bullet points under "What we treat" have now been alphabetized.
2)We have shortened the "what to expect" section so that it fits better with the map on the back page of the brochure. These changes are reflected in the uploaded file called "new brochure wording."
Hello designers. Please see our design brief, as we have recently uploaded photos for you to include in the brochure. Below are some quotes that we like. Feel free to include one or two in the brochure.
"A journey of a thousand miles begins with a single step." Wen Shaoli
"I am not what happens to me, I am what I choose to become." Emil Dorst
"Life is not about who you once were, it is about who you are right now, and the person you have the potential to become." Unknown
We have identified a number of photos and quotes from various sites that we might want to use, but don't want to buy them all in case they don't ultimately work in the design. Is it ok to upload them, but then buy them if they are used?
Drafts #2 and #5: Could you incorporate both blue and green?
draft #5: thank you for your submission. Could we see the design without the pictures of physicians in lab coats? Instead, we would like to see pictures of adults, children or families. Having some pictures of people looking unhappy, angry or stressed is fine along with happier pictures, as well. Any quotes about happiness or hopefulness would also be welcome.
draft #2: Thank you for your submission. Could you replace the picture of the older couple and replace it with children or teens? Also, could you show us another option for the layout on the interior? Or, another way of separating the sections that doesn't use the solid lines?
draft #1: Thank you for your submission. We like the way you've used blue and green throughout the brochure, and the addition of the tree was nice. Is there a way to reduce the quantity of brown used? Also, could you give us some additional variety in the pictures used, such as some in which the people are not jumping?
Do you have any website?
we need vector logo! please upload it!

```html
<!DOCTYPE html>
<html lang="en">
<head>
<meta charset="utf-8">
<title>Quiet Harbor Psychological Services – Brochure and Letterhead</title>
<link href="https://fonts.googleapis.com/css2?family=Lora:wght@400;700&family=Open+Sans:wght@400;600;700&display=swap" rel="stylesheet">
<style>
:root{
  --board:#e6e1da;
  --ink:#2b2b2b;
  --blue-deep:#0d5fa6;
  --blue:#1b7fc6;
  --blue-mid:#3e9ad6;
  --blue-soft:#8cc6ec;
  --blue-pale:#e3f1fb;
  --green:#3fae49;
  --green-light:#8cc63f;
  --white:#ffffff;
  --sky:#6fb7e8;
  --grass:#6ba83a;
}
*{box-sizing:border-box;margin:0;padding:0}
html,body{width:1200px;height:901px;overflow:hidden}
body{background:var(--board);font-family:"Open Sans",Arial,sans-serif;color:var(--ink);position:relative}
.piece{position:absolute;background:var(--white);box-shadow:0 2px 6px rgba(0,0,0,.25);overflow:hidden}
.label{position:absolute;font-size:12px;color:var(--ink);font-family:"Open Sans",Arial,sans-serif}
.photo{position:absolute}
.abs{position:absolute}
.curves{position:absolute;pointer-events:none}
.heading-bar{position:absolute;background:linear-gradient(90deg,var(--blue-deep),var(--blue-mid));color:var(--white);font-family:"Lora",Georgia,serif;font-size:15px;padding:3px 10px;border-bottom:3px solid var(--green)}
.body-text{position:absolute;font-size:7.2px;line-height:1.45}
.on-blue{color:var(--white)}
.brand-name{font-family:"Lora",Georgia,serif;font-weight:400;color:var(--green);white-space:nowrap}
.brand-dot{display:inline-block;border-radius:50%;background:var(--green);vertical-align:middle}
.brand-sub{font-family:"Lora",Georgia,serif;color:var(--blue-deep);white-space:nowrap}
.contact{font-family:"Lora",Georgia,serif;color:var(--blue-deep)}
ul.bullets{list-style:none}
ul.bullets li{padding-left:8px;position:relative}
ul.bullets li::before{content:"•";position:absolute;left:0;color:var(--green-light)}
</style>
</head>
<body>

<!-- OUTSIDE BROCHURE -->
<section class="piece outside" style="left:11px;top:11px;width:576px;height:443px">
  <!-- left panel -->
  <div class="photo" role="img" aria-label="Photo of a woman resting on a green lawn under a blue sky" style="left:0;top:0;width:192px;height:210px;background:linear-gradient(180deg,var(--sky) 0%,#bfe0f5 50%,var(--grass) 75%,#4d8a2a 100%)"></div>
  <div class="abs" style="left:0;top:210px;width:192px;height:233px;background:linear-gradient(180deg,var(--blue-deep),var(--blue))"></div>
  <div class="heading-bar" style="left:0;top:210px;width:192px">What To Expect</div>
  <p class="body-text on-blue" style="left:10px;top:242px;width:172px">During the first session, your psychologist will listen to the issues with which you are struggling and ask questions to better understand your situation. Together you will discuss how long you have been having these problems, how severe they are, and how they impact different areas of your life. Your goals, strengths and relationships will also be explored, and a plan of care will be shaped with you so that you know what comes next.<br><br>Most people say the most difficult part of therapy is getting to the first session, but that they leave feeling understood, validated, hopeful, and empowered.</p>

  <!-- middle panel -->
  <div class="photo" role="img" aria-label="Photo of a smiling family outdoors against a bright sky" style="left:192px;top:0;width:192px;height:232px;background:linear-gradient(180deg,#2d86c9 0%,var(--sky) 55%,#d8ecf8 100%)"></div>
  <p class="abs" style="left:204px;top:250px;width:170px;font-family:Lora,Georgia,serif;color:var(--blue);font-size:17px;line-height:1.15;text-align:center">Take the first step toward a better tomorrow and give us a call today.</p>
  <p class="abs contact" style="left:204px;top:340px;width:170px;font-size:10px;line-height:1.6;text-align:center">Phone: XX-XXX-XXXX<br>Fax: XX-XXX-XXXX<br><span style="font-size:13px">Address Here</span></p>

  <!-- right panel -->
  <div class="photo" role="img" aria-label="Photo of a cheerful girl under a clear blue sky" style="left:384px;top:0;width:192px;height:200px;background:linear-gradient(180deg,#1f78c1 0%,var(--sky) 60%,#cfe7f7 100%)"></div>
  <div class="abs" style="left:384px;top:226px;width:192px;text-align:center">
    <span class="brand-dot" style="width:22px;height:22px"></span>
    <div class="brand-name" style="font-size:20px;margin-top:4px">Quiet Harbor</div>
    <div style="margin:4px 14px 0;background:var(--blue);color:var(--white);font-family:Lora,Georgia,serif;font-size:10px;padding:2px 0">Psychological Services</div>
    <div class="brand-sub" style="font-size:7px;letter-spacing:2px;margin-top:3px">FOR A BETTER TOMORROW</div>
  </div>
  <p class="abs contact" style="left:384px;top:340px;width:192px;font-size:10px;line-height:1.6;text-align:center">Phone: XX-XXX-XXXX<br>Fax: XX-XXX-XXXX<br><span style="font-size:13px">Address Here</span></p>

  <svg class="curves" width="576" height="443" viewBox="0 0 576 443" aria-hidden="true" style="left:0;top:0">
    <path d="M0 209 L192 209 Q290 204 384 200 Q480 190 576 206" fill="none" stroke="var(--green)" stroke-width="3"/>
    <path d="M192 232 Q290 216 384 207 Q480 198 576 213" fill="none" stroke="var(--green-light)" stroke-width="2"/>
  </svg>
</section>
<div class="label" style="left:262px;top:460px">Outside Brochure</div>

<!-- INSIDE BROCHURE -->
<section class="piece inside" style="left:11px;top:483px;width:576px;height:398px">
  <div class="photo" role="img" aria-label="Photo of children playing together outdoors" style="left:0;top:0;width:190px;height:100px;background:linear-gradient(135deg,#5da03a,#9ccf6a 50%,#f0d9a0)"></div>
  <div class="abs" style="left:190px;top:0;width:386px;height:100px;background:linear-gradient(180deg,var(--white),var(--blue-pale))"></div>
  <div class="abs" style="left:190px;top:0;width:386px;height:26px;background:linear-gradient(90deg,var(--blue-deep),var(--blue-soft));color:var(--white);font-family:Lora,Georgia,serif;font-size:17px;padding:2px 14px">Philosophy</div>
  <p class="body-text" style="left:200px;top:32px;width:366px;color:var(--blue-deep)">Sometimes we all need a little help getting through life's challenges. At Quiet Harbor Psychological Services, we provide a supportive, non-judgmental environment where clients feel validated and respected.<br>We believe in empowering our clients and in working collaboratively with them to utilize their strengths. By offering insight into your problems and teaching new ways to cope, therapy helps clients live more fulfilling lives.</p>

  <div class="abs" style="left:0;top:100px;width:384px;height:130px;background:var(--blue-pale)"></div>
  <div class="heading-bar" style="left:0;top:100px;width:384px">How We Help</div>
  <p class="body-text" style="left:10px;top:128px;width:364px;color:var(--blue-deep)">At Quiet Harbor Psychological Services, we have a number of tools to help you and your family achieve your goals. Individual therapy helps you gain a better understanding of the factors contributing to your current difficulties and provides you with the knowledge and skills necessary to cope.<br>Child and Adolescent Therapy helps children to express their emotions and behavior, and to cope with their problems in healthy, adaptive ways.<br>Couples/Family Therapy explores the complex relationship dynamics that lead to conflict and improves communication and awareness of each other's feelings and needs.<br>Psychological and Neuropsychological Testing help to clarify cognitive, emotional, and personality factors that impact a client's life.</p>

  <div class="abs" style="left:0;top:230px;width:384px;height:168px;background:linear-gradient(180deg,var(--blue),var(--blue-deep))"></div>
  <div class="heading-bar" style="left:0;top:230px;width:384px;background:var(--blue-deep)">What We Treat</div>
  <p class="body-text on-blue" style="left:10px;top:258px;width:364px">The decision to seek help is sometimes a difficult one, and the choice of where you go for that help is important for a successful outcome.<br>Some specific problems that we can help with are:</p>
  <ul class="bullets body-text on-blue" style="left:10px;top:294px;width:180px">
    <li>Attention Deficit Hyperactivity Disorder</li>
    <li>Anxiety, Fears and Phobias</li>
    <li>Obsessive Compulsive Disorder</li>
    <li>Self Esteem/Social Skills Training</li>
    <li>Autism Spectrum Disorders</li>
    <li>Behavioral Problems</li>
    <li>Childhood and Adolescent Emotional and Behavioral problems</li>
  </ul>
  <ul class="bullets body-text on-blue" style="left:196px;top:294px;width:180px">
    <li>Family or Relationship Conflict</li>
    <li>Stress Management/Coping Skills</li>
    <li>Parenting Education and Support</li>
    <li>Personal or Professional Fulfillment</li>
    <li>Post-Traumatic Stress Disorder, Abuse</li>
    <li>School Achievement Difficulties</li>
    <li>Self-Injurious Behavior/Self Harm</li>
  </ul>

  <div class="abs" style="left:384px;top:100px;width:192px;height:298px;background:linear-gradient(180deg,var(--white) 0%,var(--white) 35%,var(--blue) 35%,var(--blue-deep) 100%)"></div>
  <div class="photo" role="img" aria-label="Photo of a thoughtful young girl" style="left:392px;top:118px;width:82px;height:82px;background:linear-gradient(135deg,#d9b48c,#a5c9e5)"></div>
  <div class="abs" style="left:480px;top:126px;width:92px;background:var(--blue);color:var(--white);font-family:Lora,Georgia,serif;font-size:15px;line-height:1.1;padding:4px 6px">Do I Need Therapy?</div>
  <p class="body-text on-blue" style="left:392px;top:208px;width:176px">Most people experience occasional sadness, anxiety, or frustration, but it may be time to consult a professional if:</p>
  <ul class="bullets body-text on-blue" style="left:392px;top:246px;width:176px">
    <li>The problem is affecting your relationships or functioning at school, home, or work.</li>
    <li>You are losing hope that your situation can change or get better.</li>
    <li>You have been unsuccessful in solving the problem on your own.</li>
    <li>You are feeling "stuck" in a certain area of your life or are unable to "get past" an incident.</li>
    <li>You have tried too many ways to cope or are engaged in self-harm behaviors.</li>
  </ul>
  <p class="body-text on-blue" style="left:392px;top:360px;width:176px">Whether you're struggling with a particular issue or just believe there should be more to life, we can help.</p>

  <svg class="curves" width="576" height="398" viewBox="0 0 576 398" aria-hidden="true" style="left:0;top:0">
    <path d="M0 100 Q190 92 384 100" fill="none" stroke="var(--green)" stroke-width="3"/>
    <path d="M384 100 Q480 110 576 100" fill="none" stroke="var(--green-light)" stroke-width="3"/>
  </svg>
</section>
<div class="label" style="left:596px;top:712px">Inside<br>Brochure</div>

<!-- FRONT FOLD -->
<section class="piece front-fold" style="left:664px;top:11px;width:144px;height:343px">
  <div class="abs" style="left:0;top:0;width:144px;height:4px;background:var(--green)"></div>
  <div class="abs" style="left:72px;top:84px;transform:translate(-50%,-50%) rotate(90deg);text-align:center">
    <div class="brand-name" style="font-size:20px"><span class="brand-dot" style="width:14px;height:14px;margin-right:6px"></span>Quiet Harbor</div>
    <div class="brand-sub" style="font-size:8px;letter-spacing:1px">PSYCHOLOGICAL SERVICES</div>
  </div>
  <div class="abs" style="left:72px;top:250px;transform:translate(-50%,-50%) rotate(90deg);text-align:left">
    <p class="contact" style="font-size:9px;line-height:1.5;white-space:nowrap">Phone: XX-XXX-XXXX<br>Fax: XX-XXX-XXXX<br><span style="font-size:11px">Address Here</span></p>
  </div>
  <svg class="curves" width="144" height="343" viewBox="0 0 144 343" aria-hidden="true" style="left:0;top:0">
    <path d="M6 0 Q16 170 6 343" fill="none" stroke="var(--green)" stroke-width="3"/>
  </svg>
</section>
<div class="label" style="left:676px;top:364px">Front Fold</div>

<!-- LETTERHEAD -->
<section class="piece letterhead" style="left:664px;top:392px;width:521px;height:478px">
  <svg class="curves" width="521" height="70" viewBox="0 0 521 70" aria-hidden="true" style="left:0;top:0">
    <path d="M0 52 Q260 40 521 58" fill="none" stroke="var(--green)" stroke-width="3"/>
    <path d="M0 57 Q260 46 521 63" fill="none" stroke="var(--blue-soft)" stroke-width="2"/>
  </svg>
  <div class="abs" style="left:18px;top:12px">
    <div class="brand-name" style="font-size:20px"><span class="brand-dot" style="width:16px;height:16px;margin-right:6px"></span>Quiet Harbor</div>
    <div class="brand-sub" style="font-size:8px;letter-spacing:1px;margin-left:22px">PSYCHOLOGICAL SERVICES</div>
  </div>
  <p class="abs contact" style="right:18px;top:8px;font-size:9px;line-height:1.5;text-align:right">Phone: XX-XXX-XXXX<br>Fax: XX-XXX-XXXX<br><span style="font-size:11px">Address Here</span></p>
  <div class="abs" style="left:0;top:408px;width:521px;height:70px;background:linear-gradient(90deg,var(--blue-deep),var(--blue))"></div>
  <ul class="bullets body-text on-blue" style="left:24px;top:416px;width:230px;font-size:6.5px">
    <li>Attention Deficit Hyperactivity Disorder</li>
    <li>Anxiety, Fears and Phobias</li>
    <li>Obsessive Compulsive Disorder</li>
    <li>Self Esteem/Social Skills Training</li>
    <li>Childhood Emotional and Behavioral problems</li>
  </ul>
  <ul class="bullets body-text on-blue" style="left:270px;top:416px;width:230px;font-size:6.5px">
    <li>Family or Relationship Conflict</li>
    <li>Stress Management/Coping Skills</li>
    <li>Parenting Education and Support</li>
    <li>Post-Traumatic Stress Disorder, Abuse</li>
    <li>Self-Injurious Behavior/Self Harm</li>
  </ul>
  <svg class="curves" width="521" height="20" viewBox="0 0 521 20" aria-hidden="true" style="left:0;top:398px">
    <path d="M0 12 Q260 2 521 10" fill="none" stroke="var(--green)" stroke-width="3"/>
  </svg>
</section>
<div class="label" style="left:676px;top:876px">Letterhead</div>

</body>
</html>
```